Literary writer needs YOUR help for an e-book cover; must look good on Brindlecart pages

This short story is about an African-American college student who thrown in jail in Baltimore, the city that just had riots. Desmond is a Harlowe College, glasses-wearing college graduate, and on the night he is arrested, he is wearing a pink Harlowe sweatshirt. He is taken in a white van to the police station and spends the weekend there. He doesn't quite believe this is happening to him because he has been insulated from the realities of race while he was a student.

The most important visual detail in the story is a $1 bill over which someone has taped triangles of the number 20 to make it look like a $20 bill. He was thrown in jail because a bar woman in a leopard skin bikini accused him of passing fake money. I did this cover myself on Pixomo, and I was thinking about a kind of noir feeling. The story is very depressing because Desmond is scared out of his mind. His weekend in jail changes his relationship with the two white friends who were out drinking with him. For anyone who has never been to Baltimore, the streets are very uneven and they are made of brick. I don't need a back cover or spine because this is just going to be an ebook. Thank you for your help!
Updates

Project Deadline Extended Reason: I don't want you to feel rushed, and I prefer to have the design be good, rather than have it be done sooner. Thank you for your help. Added Thursday, May 7, 2015

Target Market(s)

ebook buyers

Industry/Entity Type

College

Font styles to use
Serif
Sans Serif

Requirements
Must have
• Must look good at Brindlecart thumbnail size, and the title must be clearly readable
• Must also be sized correctly for the new Brindlecart ebook requirements.
• I should have stated the ebook dimensions. I'm looking for a design that is 1600 pixels wide and 2400 pixels tall. Thank you.
• The title Three Quiet Hours Past Midnight
• my name Corinne Ashworth
Nice to have
• Maybe use the "fake" $20 bill that I describe above. It might make a good cover image. Maybe use an African-American man's fingers wrapped around jail bars.
• could also have the words a short story or A short story
Should not have
• If you use the hands, they can't have any jewelry on them.

```html
<!DOCTYPE html>
<html lang="en">
<head>
<meta charset="utf-8">
<title>Three Quiet Hours Past Midnight — Cover</title>
<link rel="stylesheet" href="https://fonts.googleapis.com/css2?family=Anton&family=Cinzel:wght@700&family=Open+Sans:wght@700&display=swap">
<style>
  :root {
    --page-bg: #ededed;
    --cover-black: #000000;
    --title-yellow: #f6c500;
    --title-white: #ffffff;
    --bill-light: #d9d8d0;
    --bill-mid: #a9a89e;
    --bill-dark: #5f5e57;
    --glow-warm: rgba(246, 184, 60, 0.28);
  }
  * { margin: 0; padding: 0; box-sizing: border-box; }
  html, body {
    width: 1200px;
    height: 1200px;
    overflow: hidden;
    background: var(--page-bg);
  }
  .canvas {
    position: relative;
    width: 1200px;
    height: 1200px;
    background: var(--page-bg);
  }
  .cover {
    position: absolute;
    left: 200px;
    top: 0;
    width: 800px;
    height: 1200px;
    background: var(--cover-black);
    overflow: hidden;
  }
  .night-glow {
    position: absolute;
    left: 0;
    top: 0;
    width: 800px;
    height: 360px;
    background:
      radial-gradient(ellipse 260px 140px at 90% 10%, var(--glow-warm), transparent 70%),
      radial-gradient(ellipse 200px 120px at 10% 20%, rgba(246, 184, 60, 0.18), transparent 70%),
      radial-gradient(ellipse 300px 120px at 55% 40%, rgba(246, 184, 60, 0.12), transparent 70%);
  }
  .title-lead {
    position: absolute;
    left: 0;
    width: 800px;
    top: 150px;
    text-align: center;
    font-family: "Open Sans", sans-serif;
    font-weight: 700;
    font-size: 46px;
    line-height: 1;
    color: var(--title-yellow);
    letter-spacing: -0.5px;
  }
  .title-main {
    position: absolute;
    left: 0;
    width: 800px;
    top: 202px;
    text-align: center;
    font-family: "Anton", sans-serif;
    font-size: 214px;
    line-height: 1;
    color: var(--title-white);
    letter-spacing: -2px;
  }
  .subtitle {
    position: absolute;
    right: 80px;
    top: 458px;
    font-family: "Open Sans", sans-serif;
    font-weight: 700;
    font-size: 34px;
    line-height: 1;
    color: var(--title-yellow);
    letter-spacing: 1px;
  }
  .cover-image {
    position: absolute;
    left: 227px;
    top: 493px;
    width: 313px;
    height: 507px;
    border-radius: 6px;
    background: linear-gradient(90deg, var(--bill-dark) 0%, var(--bill-mid) 18%, var(--bill-light) 50%, var(--bill-mid) 82%, var(--bill-dark) 100%);
  }
  .author {
    position: absolute;
    left: 0;
    width: 800px;
    top: 1092px;
    text-align: center;
    font-family: "Cinzel", serif;
    font-weight: 700;
    font-size: 40px;
    line-height: 1;
    color: var(--title-yellow);
    letter-spacing: 3px;
  }
</style>
</head>
<body>
  <main class="canvas">
    <section class="cover">
      <div class="night-glow" role="img" aria-label="Soft out-of-focus warm city lights in the dark night sky"></div>
      <h1 class="title">
        <span class="title-lead">Three Quiet Hours Past</span>
        <span class="title-main">MIDNIGHT</span>
      </h1>
      <p class="subtitle">a short story</p>
      <div class="cover-image" role="img" aria-label="A rolled-up banknote whose portrait oval shows a prisoner gripping jail bars"></div>
      <p class="author">Corinne Ashworth</p>
    </section>
  </main>
</body>
</html>
```